Antique Booth hang tag design

We have just taken a booth in an Antique Mall. We have found that our off the shelf white hang tags look really tacky. We would like to create a Business Card size tag with our Company Name VONK, Booth Number 27 with designated lines to write Price, Description, Inventory Number.We specialize in Glassware and Antique Tools, but include many fun finds in our space. We do not want to include our phone numbers or names at this time since we are a vendor in the anitque mall.

Industry/Entity Type

Business

Contact Information for Business Card

This is actually for a business card style hang tag for the booth.

Font styles to use
Decorative
Script

Requirements
Must have
• Catchy design

```html
<!DOCTYPE html>
<html lang="en">
<head>
<meta charset="utf-8">
<title>VONK antiques – booth hang tag</title>
<link rel="stylesheet" href="https://fonts.googleapis.com/css2?family=Arimo:wght@700&family=Tinos:ital,wght@0,700;1,400;1,700&display=swap">
<style>
  :root {
    --tag-green: #7ea842;
    --tag-white: #ffffff;
    --ink: #111111;
    --brand-grey: #666666;
    --ghost-grey: #c6c6c6;
    --photo-dark: #cfcfcf;
    --photo-mid: #e4e4e4;
  }
  html, body {
    margin: 0;
    padding: 0;
    width: 1200px;
    height: 720px;
    overflow: hidden;
    background: var(--tag-green);
  }
  .hang-tag {
    display: block;
    width: 1200px;
    height: 720px;
  }
  .tag-field { fill: var(--tag-white); }
  .brand-name {
    font-family: "Arimo", Arial, sans-serif;
    font-weight: 700;
    font-size: 108px;
    fill: var(--brand-grey);
  }
  .brand-ghost {
    font-family: "Arimo", Arial, sans-serif;
    font-weight: 700;
    font-size: 235px;
    fill: var(--ghost-grey);
  }
  .brand-tagline {
    font-family: "Tinos", "Times New Roman", serif;
    font-style: italic;
    font-size: 35px;
    fill: var(--ink);
  }
  .write-line { stroke: var(--ink); stroke-width: 2; }
  .price-mark {
    font-family: "Tinos", "Times New Roman", serif;
    font-style: italic;
    font-weight: 700;
    font-size: 42px;
    fill: var(--ink);
  }
  .booth-number {
    font-family: "Tinos", "Times New Roman", serif;
    font-weight: 700;
    font-size: 31px;
    fill: var(--tag-white);
  }
  .string-hole { fill: var(--tag-white); }
  .string-hole-shade { fill: var(--ink); }
</style>
</head>
<body>
<svg class="hang-tag" viewBox="0 0 1200 720" xmlns="http://www.w3.org/2000/svg">
  <defs>
    <clipPath id="tag-shape">
      <ellipse cx="600" cy="357" rx="546" ry="297"/>
    </clipPath>
    <linearGradient id="glassware-tone" x1="0" y1="0" x2="1" y2="0">
      <stop offset="0" stop-color="var(--photo-mid)"/>
      <stop offset="0.35" stop-color="var(--photo-dark)"/>
      <stop offset="0.8" stop-color="var(--photo-mid)"/>
      <stop offset="1" stop-color="var(--tag-white)"/>
    </linearGradient>
  </defs>

  <ellipse class="tag-field" cx="600" cy="357" rx="546" ry="297"/>

  <g clip-path="url(#tag-shape)">
    <rect class="glassware-photo" x="54" y="60" width="498" height="600"
          fill="url(#glassware-tone)" role="img"
          aria-label="Soft black and white photograph of antique glassware"/>
    <text class="brand-ghost" transform="translate(345 82) rotate(90)" aria-hidden="true">VONK</text>
  </g>

  <g class="brand-block">
    <text class="brand-name" x="162" y="338">VONK</text>
    <text class="brand-tagline" x="473" y="376" text-anchor="end">antiques</text>
  </g>

  <g class="string-hole-group">
    <circle class="string-hole-shade" cx="110" cy="357" r="24"/>
    <circle class="string-hole" cx="106" cy="359" r="22"/>
  </g>

  <g class="write-in-lines">
    <text class="price-mark" x="640" y="198">$</text>
    <line class="write-line" x1="520" y1="201" x2="1022" y2="201"/>
    <line class="write-line" x1="520" y1="281" x2="1022" y2="281"/>
    <line class="write-line" x1="520" y1="361" x2="1022" y2="361"/>
    <line class="write-line" x1="520" y1="442" x2="1022" y2="442"/>
    <line class="write-line" x1="520" y1="523" x2="1022" y2="523"/>
  </g>

  <text class="booth-number" x="1150" y="661" text-anchor="end">booth number 27</text>
</svg>
</body>
</html>
```